Video production company website

VistaKeel Productions is a video and photography production company serving many Fortune 500 clients traveling to Hawaii and International Destinations. Our primary focus is the Corporate and Incentive group market, and offer both photography and video services. In addition, we also create custom marketing, sales, art, and real estate productions.

Target Market(s)

Corporate Incentive Travel Groups

Industry/Entity Type

Videography

Number of Pages Required

4 page

Requirements
Must have
• see doc with content. This will ultimately be needed to be a wordpress design so we can update ourselves.
Nice to have
• sleek design, professional, cutting edge, modern
Should not have
• too much Hawaii Feel, some ok but we do travel international

```html
<!DOCTYPE html>
<html lang="en">
<head>
<meta charset="utf-8">
<title>VistaKeel Productions</title>
<link rel="stylesheet" href="https://fonts.googleapis.com/css2?family=Open+Sans:wght@400;600;700&family=Roboto+Condensed:wght@400&display=swap">
<style>
:root{
  --black:#000;
  --white:#fff;
  --ink:#111;
  --muted:#666;
  --grey-band:#e8e8e8;
  --card-line:#b5b5b5;
  --bottom-bar:#2e2e2e;
  --hero-sky:#c9d6d9;
  --hero-hill:#4f7a3c;
  --hero-water:#8fb3b5;
  --hero-deck:#8a6a4a;
}
*{margin:0;padding:0;box-sizing:border-box}
html,body{width:668px;height:1200px;overflow:hidden;background:var(--white)}
body{position:relative;font-family:"Open Sans",sans-serif;color:var(--ink)}
.abs{position:absolute}
.top-strip{left:0;top:0;width:668px;height:10px;background:var(--black)}
.site-header{left:0;top:10px;width:668px;height:71px;background:var(--white)}
.brand{left:38px;top:22px;display:flex;align-items:center;gap:8px;font-size:12px;font-weight:700;color:var(--ink)}
.brand-dot{width:22px;height:22px;border-radius:50%;background:var(--black)}
.call{right:54px;top:14px;font-size:11px;color:var(--muted);display:flex;align-items:center;gap:6px}
.call strong{color:var(--ink);font-weight:700}
.main-nav{right:38px;top:47px;display:flex;gap:21px;font-size:9px;text-transform:uppercase}
.main-nav a{color:var(--ink);text-decoration:none}
.main-nav .current{font-weight:700;border-bottom:1px solid var(--ink);padding-bottom:2px}
.hero{left:0;top:81px;width:668px;height:290px;background:linear-gradient(180deg,var(--hero-sky) 0%,var(--hero-hill) 22%,var(--hero-water) 38%,#6f6d6a 60%,var(--hero-deck) 100%)}
.thumb-band{left:0;top:371px;width:668px;height:111px;background:var(--black)}
.thumb{top:396px;width:81px;height:62px;border-radius:5px}
.welcome-title{left:0;width:668px;top:507px;text-align:center;font-family:"Roboto Condensed",sans-serif;font-size:27px;letter-spacing:.5px}
.welcome-text{left:90px;width:488px;top:544px;text-align:center;font-size:9px;line-height:13px;color:var(--muted)}
.btn{border:1px solid var(--ink);background:var(--white);font-size:10px;text-transform:uppercase;display:flex;align-items:center;justify-content:center;color:var(--ink)}
.welcome-btn{left:285px;top:592px;width:98px;height:36px}
.services-band{left:0;top:640px;width:668px;height:310px;background:var(--grey-band)}
.section-title{font-family:"Roboto Condensed",sans-serif;font-size:23px;text-transform:uppercase}
.service-card{top:761px;width:174px;height:162px;border:1px solid var(--card-line)}
.service-icon{top:728px;width:66px;height:66px;border-radius:50%;border:1px solid var(--ink);background:var(--white);display:flex;align-items:center;justify-content:center}
.service-name{top:803px;width:174px;text-align:center;font-family:"Roboto Condensed",sans-serif;font-size:13px;text-transform:uppercase}
.service-text{top:829px;width:174px;text-align:center;font-size:8.5px;line-height:13px;color:var(--muted)}
.service-btn{top:876px;width:81px;height:29px}
.avatar{left:454px;width:40px;height:40px;border-radius:50%}
.quote{left:500px;width:130px;font-size:6.5px;line-height:11.5px;color:var(--muted)}
.client{left:498px;font-size:8px;font-weight:700;color:#555}
.site-footer{left:0;top:950px;width:668px;height:228px;background:var(--black);color:var(--white)}
.foot-head{font-size:14px;color:var(--white)}
.quick-links{left:44px;top:1003px;list-style:none;font-size:9px;line-height:17.5px}
.contact-row{left:248px;display:flex;align-items:flex-start;gap:8px;font-size:8.5px;line-height:13px;color:var(--white)}
.contact-icon{width:23px;height:23px;border-radius:50%;background:var(--white);display:flex;align-items:center;justify-content:center;flex:none}
.field{left:453px;width:150px;height:23px;border:1px solid var(--white);font-size:7.5px;padding:5px 4px;color:var(--white)}
.subscribe{left:452px;top:1085px;width:128px;height:26px;background:var(--white);color:var(--ink);font-weight:700;font-size:11px;display:flex;align-items:center;justify-content:center}
.bottom-bar{left:0;top:1178px;width:668px;height:22px;background:var(--bottom-bar);color:var(--white);font-size:8.5px;text-align:center;line-height:22px}
</style>
</head>
<body>
<div class="abs top-strip"></div>
<header class="abs site-header">
  <div class="abs brand"><span class="brand-dot"></span>VistaKeel Productions</div>
  <div class="abs call">CALL US NOW!
    <svg width="10" height="10" viewBox="0 0 24 24"><path fill="#111" d="M6.6 10.8a15 15 0 0 0 6.6 6.6l2.2-2.2a1 1 0 0 1 1-.25 11.4 11.4 0 0 0 3.6.6 1 1 0 0 1 1 1V20a1 1 0 0 1-1 1A17 17 0 0 1 3 4a1 1 0 0 1 1-1h3.5a1 1 0 0 1 1 1c0 1.25.2 2.45.6 3.6a1 1 0 0 1-.25 1z"/></svg>
    <strong>(808) 555.0142</strong></div>
  <nav class="abs main-nav">
    <a class="current" href="#">Home</a><a href="#">About Us</a><a href="#">Services</a><a href="#">Gallery</a><a href="#">Contact Us</a>
  </nav>
</header>

<div class="abs hero" role="img" aria-label="Large group photo of incentive travellers on a river cruise ship deck with green hills behind"></div>

<div class="abs thumb-band"></div>
<div class="abs thumb" style="left:43px;background:linear-gradient(135deg,#e0a040,#6a5a40)" role="img" aria-label="Traveller at a sunset beach"></div>
<div class="abs thumb" style="left:142px;background:linear-gradient(135deg,#6a8a4a,#c05a6a)" role="img" aria-label="Couple among flowers"></div>
<div class="abs thumb" style="left:242px;background:linear-gradient(135deg,#3a2a7a,#c04aa0)" role="img" aria-label="Evening party with coloured lights"></div>
<div class="abs thumb" style="left:339px;background:linear-gradient(180deg,#5a6ac0,#e0a0b0,#2a2a5a)" role="img" aria-label="Palm trees at sunset over calm water"></div>
<div class="abs thumb" style="left:439px;background:linear-gradient(135deg,#3ac0c0,#1a8a9a)" role="img" aria-label="Swimmer in turquoise sea"></div>
<div class="abs thumb" style="left:543px;background:linear-gradient(135deg,#c03a3a,#e8e0e0)" role="img" aria-label="Guest in a red vintage vehicle"></div>

<h1 class="abs welcome-title">WELCOME!</h1>
<p class="abs welcome-text">VistaKeel Productions is a video and photography production company serving many Fortune 500 clients in Hawaii and Internationally.&nbsp;&nbsp; Our primary focus is the Corporate and Incentive group market, and offer both photography and video services.&nbsp; In addition, we also create custom marketing, sales, art, and real estate productions.</p>
<div class="abs btn welcome-btn">Read More</div>

<section class="abs services-band"></section>
<h2 class="abs section-title" style="left:167px;top:686px">Our Services</h2>
<h2 class="abs section-title" style="left:456px;top:686px">Testimonials</h2>

<div class="abs service-card" style="left:43px"></div>
<div class="abs service-icon" style="left:97px">
  <svg width="40" height="30" viewBox="0 0 40 30"><rect x="0" y="5" width="40" height="25" rx="4" fill="#000"/><rect x="4" y="1" width="8" height="5" fill="#000"/><rect x="14" y="1" width="12" height="6" rx="2" fill="#000"/><circle cx="22" cy="17" r="8" fill="#fff"/><circle cx="22" cy="17" r="5" fill="#000"/><rect x="4" y="9" width="5" height="3" fill="#fff"/></svg>
</div>
<div class="abs service-name" style="left:43px">Photography</div>
<p class="abs service-text" style="left:43px">Lorem Ipsum is simply dummy text of the printing and typesetting industry.Lorem Ipsum has been the industry</p>
<div class="abs btn service-btn" style="left:81px">Read More</div>

<div class="abs service-card" style="left:249px"></div>
<div class="abs service-icon" style="left:302px">
  <svg width="38" height="30" viewBox="0 0 38 30"><circle cx="8" cy="6" r="5" fill="#000"/><circle cx="19" cy="6" r="5" fill="#000"/><rect x="1" y="11" width="26" height="18" rx="3" fill="#000"/><path d="M27 18l10-6v16l-10-6z" fill="#000"/></svg>
</div>
<div class="abs service-name" style="left:249px">Videography</div>
<p class="abs service-text" style="left:249px">Lorem Ipsum is simply dummy text of the printing and typesetting industry.Lorem Ipsum has been the industry</p>
<div class="abs btn service-btn" style="left:295px">Read More</div>

<div class="abs avatar" style="top:732px;background:linear-gradient(135deg,#d0d8e0,#8a6a5a)" role="img" aria-label="Client portrait"></div>
<p class="abs quote" style="top:727px">"Lorem Ipsum is simply dummy text of the printing and typesetting industry. Lorem Ipsum has been the industry's standard dummy text ever since the 1500s"</p>
<div class="abs client" style="top:783px">– Client Name</div>
<div class="abs avatar" style="top:815px;background:linear-gradient(135deg,#c08a3a,#4a5a7a)" role="img" aria-label="Client portrait"></div>
<p class="abs quote" style="top:810px">"Lorem Ipsum is simply dummy text of the printing and typesetting industry. Lorem Ipsum has been the industry's standard dummy text ever since the 1500s"</p>
<div class="abs client" style="top:866px">– Client Name</div>

<footer class="abs site-footer"></footer>
<h3 class="abs foot-head" style="left:44px;top:974px;font-weight:400">Quick links</h3>
<ul class="abs quick-links" style="color:#fff"><li>Home</li><li>About us</li><li>Services</li><li>Gallery</li><li>Contact</li></ul>

<h3 class="abs foot-head" style="left:248px;top:974px;font-weight:400">Contact us</h3>
<div class="abs contact-row" style="top:1007px"><span class="contact-icon"><svg width="12" height="12" viewBox="0 0 24 24"><path fill="#000" d="M12 3 2 12h3v8h5v-6h4v6h5v-8h3z"/></svg></span><span>VistaKeel Productions, LLC<br>P.O. Box 402-118<br>Haleiwa HI 96712</span></div>
<div class="abs contact-row" style="top:1056px;align-items:center"><span class="contact-icon"><svg width="12" height="12" viewBox="0 0 24 24"><path fill="#000" d="M6.6 10.8a15 15 0 0 0 6.6 6.6l2.2-2.2a1 1 0 0 1 1-.25 11.4 11.4 0 0 0 3.6.6 1 1 0 0 1 1 1V20a1 1 0 0 1-1 1A17 17 0 0 1 3 4a1 1 0 0 1 1-1h3.5a1 1 0 0 1 1 1c0 1.25.2 2.45.6 3.6a1 1 0 0 1-.25 1z"/></svg></span><span>555.0142</span></div>
<div class="abs contact-row" style="top:1092px;align-items:center"><span class="contact-icon"><svg width="12" height="12" viewBox="0 0 24 24"><rect x="4" y="9" width="16" height="11" rx="1" fill="#000"/><rect x="7" y="3" width="10" height="6" fill="none" stroke="#000" stroke-width="2"/><rect x="8" y="12" width="8" height="2" fill="#fff"/><rect x="8" y="15" width="8" height="2" fill="#fff"/></svg></span><span>555.0197</span></div>
<div class="abs contact-row" style="top:1128px;align-items:center"><span class="contact-icon"><svg width="12" height="12" viewBox="0 0 24 24"><rect x="3" y="6" width="18" height="12" rx="1" fill="none" stroke="#000" stroke-width="2"/><path d="M3 7l9 6 9-6" fill="none" stroke="#000" stroke-width="2"/></svg></span><span>info@vistakeelpro.com</span></div>

<h3 class="abs foot-head" style="left:454px;top:974px;font-family:'Roboto Condensed',sans-serif;font-weight:400">NEWSLETTER</h3>
<div class="abs field" style="top:1015px">Enter Name</div>
<div class="abs field" style="top:1050px">Email id</div>
<div class="abs subscribe">SUBSCRIBE</div>

<div class="abs bottom-bar">©<strong>VISTAKEELPRODUCTIONS</strong> - 2016. All Rights Reserved.</div>
</body>
</html>
```